Tri-Fold Menu of Services for our Eyelash and Skin Care Spa

We need a beautiful spa service menu for our upscale spa in St. Charles Missouri. We specialize in providing treatments that are specific to the clients needs. Our services are eyelash extensions, skin care treatments, full body waxing and makeup application. Our spa colors are dark purples and greys and we are not opposed to additional colors that would complement those colors. We do a lot of eyelash extensions and while we do what those services listed we would like the skin care treatments to be in an area that would be noticed first. One of the attachments lists all of our services, descriptions and prices (please be sure to include all services and pricing. descriptions if possible). And our website has more information about us if needed. The website was not professionally done. So it DOESN'T represent our style exactly.

I HAVE ATTACHED A FEW PHOTOS BUT THEY DON'T HAVE TO BE USED.

Target Market(s)

women who would like to look their best, 35-55, annual income of 100,000+, she is usually busy and her children (if she has any) are high school age or older.

Industry/Entity Type

It Service

Font styles to use
Serif
Sans Serif

Requirements
Must have
• Must list all of our services. If it works to have the descriptions that would be great.
Nice to have
• If it works to have the descriptions of each service that would be great.

```html
<!DOCTYPE html>
<html lang="en">
<head>
<meta charset="utf-8">
<title>Velora Lash &amp; Skin Spa – Menu of Services</title>
<link href="https://fonts.googleapis.com/css2?family=Kreon:wght@300;400&family=Source+Sans+3:wght@400;600&display=swap" rel="stylesheet">
<style>
  :root{
    --plum:#472a47;
    --plum-mid:#6a4a68;
    --plum-soft:#8c7089;
    --grey:#cfcfcf;
    --grey-light:#e6e6e6;
    --ink:#2a2a2a;
    --white:#ffffff;
    --skin-a:#e9d3c6;
    --skin-b:#c9a58f;
  }
  html,body{margin:0;padding:0;overflow:hidden;background:var(--white);}
  .brochure{position:relative;width:1200px;height:927px;overflow:hidden;background:var(--white);font-family:"Source Sans 3",Arial,sans-serif;color:var(--ink);}
  .shapes{position:absolute;inset:0;}
  .panel{position:absolute;top:0;height:927px;}
  .panel--services{left:0;width:395px;overflow:hidden;}
  .panel--contact{left:395px;width:405px;}
  .panel--cover{left:800px;width:400px;}

  .section-title{position:absolute;left:42px;top:44px;margin:0;font-family:"Kreon",Georgia,serif;font-weight:300;font-size:22px;letter-spacing:.5px;color:var(--plum);text-transform:uppercase;}
  .service-list{position:absolute;left:42px;top:86px;width:328px;margin:0;padding:0;list-style:none;}
  .service{margin-bottom:18px;font-size:12px;line-height:15.5px;}
  .service__name{font-weight:600;color:var(--plum);}
  .service__price{color:var(--ink);}
  .service__desc{margin:0;hyphens:auto;}

  .contact{position:absolute;left:48px;top:68px;font-family:"Kreon",Georgia,serif;color:var(--white);text-transform:uppercase;}
  .contact h2{margin:0 0 10px;font-weight:300;font-size:19px;letter-spacing:.5px;}
  .contact p{margin:0;font-size:13px;line-height:23.5px;font-weight:300;letter-spacing:.3px;}
  .contact .gap{margin-top:22px;}
  .hours{position:absolute;left:48px;top:262px;font-family:"Kreon",Georgia,serif;color:var(--white);text-transform:uppercase;}
  .hours h2{margin:0 0 6px;font-weight:300;font-size:19px;letter-spacing:.5px;}
  .hours table{border-collapse:collapse;font-size:12.5px;font-weight:300;letter-spacing:.3px;}
  .hours td{padding:0;height:23.5px;}
  .hours td:first-child{width:163px;}

  .brand{position:absolute;font-family:"Kreon",Georgia,serif;font-weight:300;line-height:1;margin:0;}
  .brand--cover{left:62px;top:118px;color:var(--plum);font-size:36px;width:300px;}
  .brand--back{left:52px;top:722px;color:var(--white);font-size:34px;width:300px;}
</style>
</head>
<body>
<main class="brochure">
  <svg class="shapes" width="1200" height="927" viewBox="0 0 1200 927">
    <defs>
      <linearGradient id="skin-left" x1="0" y1="0" x2="1" y2="1">
        <stop offset="0" stop-color="#f1e4dc"/>
        <stop offset=".5" stop-color="#e9d3c6"/>
        <stop offset="1" stop-color="#c9a58f"/>
      </linearGradient>
      <linearGradient id="skin-right" x1="0" y1="0" x2="1" y2="1">
        <stop offset="0" stop-color="#f4ebe5"/>
        <stop offset=".55" stop-color="#e9d3c6"/>
        <stop offset="1" stop-color="#b89482"/>
      </linearGradient>
    </defs>

    <path d="M0 492 C110 470 250 480 395 520 L395 927 L0 927 Z" fill="url(#skin-left)" role="img" aria-label="Photo of a facial skin treatment with a handheld device"/>
    <path d="M0 470 C120 455 260 470 395 505 L395 520 C250 482 110 474 0 494 Z" fill="var(--grey)"/>
    <path d="M0 496 C110 474 250 484 395 522 L395 540 C250 500 110 492 0 512 Z" fill="var(--plum)"/>

    <rect x="395" y="0" width="405" height="927" fill="var(--plum)"/>

    <path d="M800 318 C900 300 1050 285 1168 283 C1060 305 920 330 800 345 Z" fill="var(--plum-mid)"/>
    <path d="M800 345 C920 330 1060 305 1168 283 C1060 318 930 355 800 372 Z" fill="var(--grey)"/>
    <path d="M932 421 C1010 395 1110 385 1200 386 L1200 392 C1110 395 1020 405 932 421 Z" fill="var(--grey-light)"/>
    <path d="M932 421 C1010 392 1110 378 1200 380 L1200 400 C1110 398 1020 405 932 421 Z" fill="var(--plum-soft)"/>

    <path d="M800 528 C900 515 1060 505 1200 518 L1200 927 L800 927 Z" fill="url(#skin-right)" role="img" aria-label="Photo of a relaxing facial massage on a client lying on white towels"/>
  </svg>

  <section class="panel panel--services">
    <h2 class="section-title">Facial &amp; Skin Treatments</h2>
    <ul class="service-list">
      <li class="service">
        <span class="service__name">Essential Deep Cleansing Treatment</span>
        <span class="service__price">$65 60 mins</span>
        <p class="service__desc">This relaxing, purifying treatment consists of steaming, exfoliation, and an intense deepercleansing of clogged pores. A skintype specific ampoule is gently massaged into the skin of your face, neck, and decollete, followed by a therapist selected mask. Beneficial for all skin types.</p>
      </li>
      <li class="service">
        <span class="service__name">Mini Facial</span>
        <span class="service__price">$48 (30 mins)</span>
        <p class="service__desc">This express facial is ideal for those on the go. Your skin is cleansed, lightly exfoliated and gently massaged. A pore-refining mask is then applied, followed by a veil of light moisturizer.</p>
      </li>
      <li class="service">
        <span class="service__name">Aromatherapy Facial</span>
        <span class="service__price">&nbsp;$75 (60 mins)</span>
        <p class="service__desc">Our Aromatherapy facial will naturally enhance the<br>facial benefits using fragrant oils extracted<br>from flowers, fruits and herbs.</p>
      </li>
    </ul>
  </section>

  <section class="panel panel--contact">
    <div class="contact">
      <h2>Contact:</h2>
      <p>2240 Meadowlark Rd</p>
      <p>St. Charles MO 63300</p>
      <p>(Across Hwy 94 from Summit Fitness)</p>
      <p class="gap">Phone: 636-555-0142</p>
      <p>Email: veloraspa.stl@mail.com</p>
    </div>
    <div class="hours">
      <h2>Opening Times:</h2>
      <table>
        <tr><td>Tuesday</td><td>11:00am - 6:00pm</td></tr>
        <tr><td>Wednesday- Friday</td><td>11:00am-8:00pm</td></tr>
        <tr><td>Saturday</td><td>10:00am - 3:00pm</td></tr>
        <tr><td>Sunday-Monday</td><td>Closed</td></tr>
      </table>
    </div>
    <p class="brand brand--back">Velora<br>Lash &amp; Skin Spa</p>
  </section>

  <section class="panel panel--cover">
    <h1 class="brand brand--cover">Velora<br>Lash &amp; Skin Spa</h1>
  </section>
</main>
</body>
</html>
```